" Assessoria e consultoria de projetos agropecuários com foco em bovinos. DIFERENCIAIS ? Atendimento personalizado; ? Foco em processos; Melhoria continua - metodologia LEAN ? Foco no cliente e na qualidade do serviço; ? Acompanhamento dos resultados gerados pela consultoria; ? Serviço com conhecimento agregado. Atendimento personalizado: A Brota enxerga a necessidade do contato personalizado com o cliente, demonstrando constantemente que a empresa está interessada em ajudá-lo e trazer soluções para seus problemas. ? Foco em processos: Como a maioria das empresas que prestam consultoria na área estão mais voltadas para TÉCNICAS animal, o foco em processos e gestao por processos torna-se um diferencial da Brota. A empresa poderia aproveitar essa vantagem divulgando a importância do gerenciamento eficaz nas fazendas através dos processos agropecuários. ? Foco no cliente e na qualidade do serviço: Através do atendimento personalizado, o consultor da Brota tem a responsabilidade de manter o comprometimento com o cliente e com a qualidade dos serviços entregues. Assim, a empresa cria uma boa relação com os consumidores, fidelizando-os. ? Acompanhamento dos resultados gerados pela consultoria: Além de prestar consultoria, a Empresa auxilia o cliente a implementar as técnicas e soluções, fazendo o acompanhamento de resultados com indicadores. ? Serviço com maior valor agregado: Através da constante busca por conhecimento na área, a qualidade dos projetos entregues será cada vez maior, consequentemente tornando-os mais eficazes e eficientes. "

```html
<!DOCTYPE html>
<html lang="pt-BR">
<head>
<meta charset="utf-8">
<title>Brota – Assinatura de e-mail</title>
<link rel="stylesheet" href="https://fonts.googleapis.com/css2?family=Roboto:wght@400;500;700&display=swap">
<style>
  :root {
    --page-bg: #eef0f2;
    --navy: #0e1b3a;
    --green: #1f9b4a;
    --silver-light: #e6e8eb;
    --silver-dark: #8d939b;
    --text-light: #ffffff;
    --brand-grey: #c6cad0;
  }
  * { margin: 0; padding: 0; box-sizing: border-box; }
  html, body { width: 1200px; height: 1200px; overflow: hidden; }
  body {
    background: var(--page-bg);
    font-family: "Roboto", Arial, sans-serif;
    position: relative;
  }
  .signature {
    position: absolute;
    left: 67px;
    top: 508px;
    width: 1066px;
    height: 186px;
    background: var(--navy);
    border-radius: 4px 28px 4px 28px;
    overflow: hidden;
    color: var(--text-light);
  }
  .contact-list { position: absolute; left: 44px; top: 22px; list-style: none; }
  .contact-item {
    display: flex; align-items: flex-start; gap: 16px;
    font-size: 23px; line-height: 28px; margin-bottom: 12px;
  }
  .contact-icon { width: 28px; height: 28px; flex: none; }
  .person {
    position: absolute; left: 404px; top: 66px;
    padding-left: 24px;
    border-left: 7px solid var(--green);
  }
  .person-name { font-weight: 700; font-size: 27px; line-height: 32px; letter-spacing: 0.3px; }
  .person-role { font-size: 24px; line-height: 30px; }
  .brand {
    position: absolute; left: 780px; top: 58px;
    display: flex; align-items: center; gap: 18px;
  }
  .brand-dot { width: 26px; height: 26px; border-radius: 50%; background: var(--green); }
  .brand-name {
    font-size: 54px; font-weight: 500; letter-spacing: 10px;
    color: var(--brand-grey); text-transform: uppercase;
  }
  .bottom-bands { position: absolute; left: 0; bottom: 0; width: 1066px; height: 24px; }
</style>
</head>
<body>
  <section class="signature">
    <ul class="contact-list">
      <li class="contact-item">
        <svg class="contact-icon" viewBox="0 0 28 28"><circle cx="14" cy="14" r="14" fill="#1f9b4a"/><rect x="10" y="7" width="8" height="14" rx="1.5" fill="#0e1b3a"/><rect x="11.5" y="9" width="5" height="9" fill="#1f9b4a"/></svg>
        <span>(00) 0000-0000</span>
      </li>
      <li class="contact-item">
        <svg class="contact-icon" viewBox="0 0 28 28"><circle cx="14" cy="14" r="14" fill="#1f9b4a"/><rect x="7.5" y="9.5" width="13" height="9" rx="1" fill="#0e1b3a"/><path d="M8 10l6 5 6-5" fill="none" stroke="#1f9b4a" stroke-width="1.4"/></svg>
        <span>contato@exemplo.com</span>
      </li>
      <li class="contact-item">
        <svg class="contact-icon" viewBox="0 0 28 28"><circle cx="14" cy="14" r="14" fill="#1f9b4a"/><path d="M14 6a5 5 0 0 0-5 5c0 4 5 10 5 10s5-6 5-10a5 5 0 0 0-5-5z" fill="#0e1b3a"/><circle cx="14" cy="11" r="2" fill="#1f9b4a"/></svg>
        <span>Rua exemplo, 000<br>cidade-UF, CEP: 0000-000</span>
      </li>
    </ul>

    <div class="person">
      <p class="person-name">NOME E SOBRENOME</p>
      <p class="person-role">Cargo/Função</p>
    </div>

    <div class="brand">
      <span class="brand-dot"></span>
      <span class="brand-name">Brota</span>
    </div>

    <svg class="bottom-bands" viewBox="0 0 1066 24" preserveAspectRatio="none">
      <defs>
        <linearGradient id="silver" x1="0" x2="1" y1="0" y2="0">
          <stop offset="0" stop-color="#8d939b"/>
          <stop offset="0.45" stop-color="#e6e8eb"/>
          <stop offset="1" stop-color="#9aa0a7"/>
        </linearGradient>
      </defs>
      <polygon points="0,10 500,10 490,18 0,18" fill="url(#silver)"/>
      <polygon points="510,12 1066,12 1066,18 504,18" fill="#1f9b4a"/>
    </svg>
  </section>
</body>
</html>
```